IT Company Business Card design

Brisk Loop is a new computer solutions business focusing on setting up servers and computer systems for small to medium sized businesses.

A business client will either request a solution, or support for a current system and we will turn up on site to provide these services.

We are bast in Christchurch, New Zealand.

We are looking for unique business card's that stand out and show off the business in a professional light.

Open to all idea's etc.

Industry/Entity Type

Computer

Requirements
Must have
• Business Logo (AI file attached)
Employee Name
Business title
Business landline number
Cell phone number
Email
Web URL
Nice to have
• Could be nice to have some keywords (possibly on the back) such as:

Business IT solutions
Network installations
Phone solutions
Server management
Software diagnostics

The above is not needed, just an idea.

```html
<!DOCTYPE html>
<html lang="en">
<head>
<meta charset="utf-8">
<title>Brisk Loop – Business Card Concepts</title>
<link rel="stylesheet" href="https://fonts.googleapis.com/css2?family=Source+Sans+3:wght@300;400;600;700&display=swap">
<style>
  :root {
    --stage: #e9e6e1;
    --white: #ffffff;
    --ink: #1c1c24;
    --grey: #6f7178;
    --navy: #23306d;
    --blue-mid: #2e6fb4;
    --sky: #42b3e8;
    --royal: #2d5fae;
    --glow: #3ab6e8;
    --label: #3a3a3a;
    --faint: rgba(255,255,255,.16);
  }
  * { box-sizing: border-box; margin: 0; padding: 0; }
  html, body {
    width: 1200px; height: 770px; overflow: hidden;
    background: var(--stage);
    font-family: "Source Sans 3", "Myriad Pro", Arial, sans-serif;
  }
  .sheet { position: relative; width: 1200px; height: 770px; }
  .card {
    position: absolute; width: 565px; height: 323px; overflow: hidden;
    box-shadow: 0 1px 3px rgba(0,0,0,.25);
  }
  .card--front { left: 27px; top: 22px; background: var(--white); }
  .card--sky { left: 614px; top: 22px; background: var(--sky); }
  .card--glow { left: 25px; top: 395px;
    background: radial-gradient(circle at 61% 48%, var(--glow) 0%, #2f7cc0 38%, #27508f 70%, #223f7c 100%); }
  .card--royal { left: 614px; top: 395px; background: var(--royal); }

  .front-art { position: absolute; inset: 0; }
  .brand {
    position: absolute; left: 15px; top: 118px;
    display: flex; align-items: center; gap: 13px;
  }
  .brand__dot { width: 80px; height: 80px; border-radius: 50%; background: var(--blue-mid); }
  .brand__divider { width: 1px; height: 86px; background: #9a9ca3; }
  .brand__name { font-size: 27px; font-weight: 400; letter-spacing: 1.5px; color: var(--ink); line-height: 1; white-space: nowrap; }
  .brand__tagline { font-size: 15.5px; font-weight: 400; color: var(--grey); letter-spacing: .4px; margin-top: 6px; white-space: nowrap; }

  .contact {
    position: absolute; right: 19px; top: 60px; text-align: right; color: var(--white);
  }
  .contact__name { font-size: 18px; font-weight: 700; line-height: 1.2; }
  .contact__title { font-size: 13px; font-weight: 400; margin-bottom: 19px; }
  .contact__line { font-size: 13.5px; line-height: 24px; display: flex; justify-content: flex-end; align-items: center; gap: 5px; }
  .contact__line svg { width: 12px; height: 12px; }
  .contact__address { margin-top: 16px; font-size: 13.5px; line-height: 20px; }

  .back__name {
    position: absolute; left: 0; right: 0; top: 128px; text-align: center;
    color: var(--faint); font-size: 40px; font-weight: 400; letter-spacing: 4px;
  }
  .back__url {
    position: absolute; left: 0; right: 0; bottom: 22px; text-align: center;
    color: var(--white); font-size: 18px; letter-spacing: 3.4px; font-weight: 400;
  }
  .label { position: absolute; font-size: 24px; color: var(--label); font-weight: 400; }
  .label--1 { left: 828px; top: 352px; }
  .label--2 { left: 226px; top: 726px; }
  .label--3 { left: 824px; top: 726px; }
</style>
</head>
<body>
<main class="sheet">

  <section class="card card--front">
    <svg class="front-art" viewBox="0 0 565 323" aria-hidden="true">
      <defs>
        <radialGradient id="panelShade" cx="0.28" cy="0.5" r="0.75">
          <stop offset="0" stop-color="#3fa3dc"/>
          <stop offset="0.45" stop-color="#2a5fa5"/>
          <stop offset="1" stop-color="#1d2a66"/>
        </radialGradient>
      </defs>
      <circle cx="600" cy="168" r="292" fill="#111"/>
      <circle cx="606" cy="150" r="282" fill="#fff"/>
      <circle cx="616" cy="140" r="278" fill="url(#panelShade)"/>
    </svg>

    <div class="brand">
      <span class="brand__dot"></span>
      <span class="brand__divider"></span>
      <div>
        <div class="brand__name">BRISK LOOP</div>
        <div class="brand__tagline">Your It Department</div>
      </div>
    </div>

    <div class="contact">
      <div class="contact__name">Employee Name</div>
      <div class="contact__title">title</div>
      <div class="contact__line">
        <svg viewBox="0 0 12 12"><path d="M3 1 L5 3.5 L4 5 Q5 7 7 8 L8.5 7 L11 9 L9.5 11 Q4 10 1 3 Z" fill="#fff"/></svg>123-456-0789</div>
      <div class="contact__line">
        <svg viewBox="0 0 12 12"><rect x="3" y="0.5" width="6" height="11" rx="1" fill="#fff"/><rect x="4" y="2" width="4" height="4" fill="#23306d"/></svg>123-456-0789</div>
      <div class="contact__line">
        <svg viewBox="0 0 12 12"><rect x="0.5" y="2.5" width="11" height="8" fill="#fff"/><path d="M0.5 2.5 L6 7 L11.5 2.5" stroke="#23306d" stroke-width="1" fill="none"/></svg>info@briskloop.com</div>
      <div class="contact__line">
        <svg viewBox="0 0 12 12"><circle cx="6" cy="6" r="5" stroke="#fff" stroke-width="1.2" fill="none"/><ellipse cx="6" cy="6" rx="2" ry="5" stroke="#fff" stroke-width="1" fill="none"/><path d="M1 6 H11" stroke="#fff" stroke-width="1"/></svg>www.briskloop.com</div>
      <div class="contact__address">Street Name, City Name<br>State Zip Code</div>
    </div>
  </section>

  <section class="card card--sky">
    <p class="back__name">BRISK LOOP</p>
    <p class="back__url">www.briskloop.com</p>
  </section>
  <p class="label label--1">Option-1</p>

  <section class="card card--glow">
    <p class="back__name">BRISK LOOP</p>
    <p class="back__url">www.briskloop.com</p>
  </section>
  <p class="label label--2">Option-2</p>

  <section class="card card--royal">
    <p class="back__name">BRISK LOOP</p>
    <p class="back__url">www.briskloop.com</p>
  </section>
  <p class="label label--3">Option-3</p>

</main>
</body>
</html>
```